Quillstar Lottery Landing Page -

We are looking for a unique Landing Page design that makes users want to subscribe!
Banner artwork, quillstar promo video (already created), subscription info, product highlights. Why users would want to subscribe.
The initial work was done in PHP. I will provide the website in it's current state in a zip file. The website can be run locally with XAMPP.
Target Market(s)
Anyone who plays the lottery and wants to win more!
Industry/Entity Type
Lottery, USA and Canada (More Countries will be added soon)
Coding
Coded - Design and coding required
Other font styles liked:
- Unzip the the work we have currently done and this should give you a good idea of what direction we are going. We love this theme but now we just need to
Requirements
Must have
- After you unzip the quillstar.zip and open the site using XAMPP

```html
<!DOCTYPE html>
<html lang="en">
<head>
<meta charset="utf-8">
<title>Quillstar Lottery Software</title>
<link href="https://fonts.googleapis.com/css2?family=Heebo:wght@400;500;700;800&display=swap" rel="stylesheet">
<style>
:root{
  --bg:#0f1d28;
  --bg-hero:#1c2e3c;
  --bg-band:#13283a;
  --orange:#f68a0f;
  --brand:#e8321f;
  --white:#ffffff;
  --text:#e6ebef;
  --wine:#4e0808;
  --line:#2c3c48;
}
*{margin:0;padding:0;box-sizing:border-box}
html,body{width:1200px;height:2780px;overflow:hidden;background:var(--bg);font-family:"Heebo",sans-serif;color:var(--white)}
.page{position:relative;width:1200px;height:2780px}
.abs{position:absolute}

.hero{left:0;top:0;width:1200px;height:734px;background:radial-gradient(ellipse at 78% 45%,#2f5a86 0%,#1f3a55 35%,var(--bg-hero) 70%)}
.brand{display:flex;align-items:center;gap:10px;font-weight:800;color:var(--brand)}
.brand-dot{width:34px;height:34px;border-radius:50%;background:var(--brand)}
.hero .brand{left:112px;top:30px;font-size:30px}
.join{left:822px;top:20px;width:130px;height:38px;border-radius:19px;background:var(--orange);font-size:13px;font-weight:700;display:flex;align-items:center;justify-content:center}
.burger{left:994px;top:28px;width:28px}
.burger span{display:block;height:3px;background:var(--white);margin-bottom:6px}
.eyebrow{left:111px;top:250px;color:var(--orange);font-size:19px;font-weight:700}
.hero-title{left:110px;top:284px;font-size:44px;font-weight:800;line-height:50px;width:460px}
.hero-copy{left:111px;top:393px;font-size:16px;line-height:26px;width:400px;color:var(--text)}
.btn{background:var(--orange);border-radius:4px;font-weight:700;display:flex;align-items:center;justify-content:center;font-size:16px}
.get{left:111px;top:464px;width:165px;height:56px}
.play{left:293px;top:469px;display:flex;align-items:center;gap:12px;font-size:16px;font-weight:700}
.play-ring{width:46px;height:46px;border:1px solid var(--orange);border-radius:50%;display:flex;align-items:center;justify-content:center}
.hero-art{left:510px;top:95px;width:680px;height:540px;border-radius:50%;background:radial-gradient(circle at 50% 50%,#5b7fc0 0%,#7340a8 45%,rgba(40,70,110,0) 72%)}

.section-title{width:1200px;left:0;text-align:center;font-weight:800;font-size:35px}
.products-title{top:802px}
.card{top:900px;width:191px;height:194px;display:flex;align-items:flex-end;padding:14px;font-size:16px;font-weight:700;line-height:26px}
.c1{left:115px;background:linear-gradient(160deg,#2f6a3a,#8a6a1a 50%,#1a2a25)}
.c3{left:680px;background:linear-gradient(170deg,#c06a20,#1f6a3a 45%,#1a3028)}
.c4{left:895px;background:linear-gradient(160deg,#3040a8,#8a2a90 50%,#201a40)}
.feature{left:328px;top:881px;width:330px;height:231px;background:radial-gradient(circle at 60% 55%,#6a1010,var(--wine));padding:54px 22px 0}
.feature h3{font-size:21px;font-weight:700;margin-bottom:8px}
.feature p{font-size:15px;line-height:26px;color:var(--text)}
.feature a{display:block;margin-top:6px;color:var(--orange);font-size:16px;font-weight:500;text-decoration:none}

.video-band{left:0;top:1197px;width:1200px;height:516px;background:var(--bg-band)}
.video-title{top:1255px}
.video{left:138px;top:1340px;width:928px;height:515px;border:4px solid var(--orange);border-radius:4px;background:linear-gradient(180deg,#6a86e0 0%,#8a9cf0 55%,#b8707a 100%)}
.video-play{left:572px;top:1570px;width:60px;height:60px;border-radius:50%;background:var(--orange);display:flex;align-items:center;justify-content:center}

.why-title{top:1935px}
.why-copy{left:210px;top:1996px;width:780px;text-align:center;font-size:16px;line-height:26px;color:var(--text)}
.learn{left:522px;top:2130px;width:155px;height:52px}

.footer{left:0;top:2270px;width:1200px;height:510px;background:radial-gradient(ellipse at 50% 40%,#1b2e3d,var(--bg) 70%)}
.footer .brand{left:125px;top:2340px;font-size:40px}
.footer .brand .brand-dot{width:48px;height:48px}
.col-title{font-size:23px;font-weight:500}
.links{list-style:none;font-size:16px;line-height:30px;color:var(--text)}
.news-title{left:591px;top:2345px;font-size:31px;font-weight:700}
.field{left:592px;top:2412px;width:322px;height:40px;border-bottom:1px solid #5b6a74;font-size:16px;color:var(--text);display:flex;justify-content:space-between;padding-top:8px}
.contact{top:2487px;font-size:15px;font-weight:500}
.socials{left:968px;top:2492px;display:flex;gap:14px}
.socials span{width:14px;height:14px;border-radius:50%;background:var(--orange)}
.rule{left:113px;top:2682px;width:978px;height:1px;background:var(--line)}
.copy{left:0;top:2712px;width:1200px;text-align:center;font-size:16px;color:var(--text)}
</style>
</head>
<body>
<div class="page">
  <section class="abs hero"></section>
  <div class="abs brand"><span class="brand-dot"></span>Quillstar</div>
  <div class="abs join">JOIN NOW</div>
  <div class="abs burger"><span></span><span></span><span></span></div>
  <div class="abs hero-art" role="img" aria-label="Colourful lottery balls and lottery tickets on a radiant blue background"></div>
  <p class="abs eyebrow">PLAY SMARTER WIN MORE!</p>
  <h1 class="abs hero-title">QUILLSTAR LOTTERY SOFTWARE</h1>
  <p class="abs hero-copy">Lorem ipsum dolor sit amet, consectetur adipiscing elit, sed do eiusmod tempor incididunt ut</p>
  <div class="abs btn get">GET STARTED</div>
  <div class="abs play"><span class="play-ring"><svg width="14" height="16" viewBox="0 0 14 16"><path d="M1 1l12 7-12 7z" fill="#f68a0f"/></svg></span>PLAY NOW</div>

  <h2 class="abs section-title products-title">OUR PRODUCTS</h2>
  <div class="abs card c1" role="img" aria-label="Lotto ticket with coins and lottery balls">PILLS-STARBALL</div>
  <div class="abs feature">
    <h3>STAR BALL RESULT</h3>
    <p>Lorem ipsum dolor sit amet, consec-tetur adipiscing elit, sed do eiusmod tempor incididunt</p>
    <a href="#">Learn More</a>
  </div>
  <div class="abs card c3" role="img" aria-label="Billiard balls on green felt">STAR BALL<br>INFORMATION</div>
  <div class="abs card c4" role="img" aria-label="Row of colourful bowling balls">STAR BALL NEWS</div>

  <div class="abs video-band"></div>
  <h2 class="abs section-title video-title">OUR QUILLSTAR LOTTERY VIDEO</h2>
  <div class="abs video" role="img" aria-label="Promo video still: hand holding a phone with the app screen in front of a window onto a street of houses"></div>
  <div class="abs video-play"><svg width="16" height="18" viewBox="0 0 16 18"><path d="M1 1l14 8-14 8z" fill="#fff"/></svg></div>

  <h2 class="abs section-title why-title">WHY USERS WOULD WANT TO SUBSCRIBE</h2>
  <p class="abs why-copy">Lorem ipsum dolor sit amet, consectetur adipiscing elit, sed do eiusmod tempor incididunt ut labore et dolore magna aliqua. Quis ipsum suspendisse ultrices gravida. Risus commodo viverra maecenas accumsan lacus vel facilisis. Lorem ipsum dolor sit amet, consectetur adipiscing elit, sed do eiusmod tempor incididunt ut labore et dolore magna aliqua. Quis ipsum suspendisse ultrices gravida.</p>
  <div class="abs btn learn">LEARN MORE</div>

  <footer class="abs footer"></footer>
  <div class="abs brand"><span class="brand-dot"></span>Quillstar</div>
  <h3 class="abs col-title" style="left:124px;top:2434px">Quick Link</h3>
  <ul class="abs links" style="left:127px;top:2478px"><li>Home</li><li>About Us</li><li>Why User</li><li>Contact</li></ul>
  <h3 class="abs col-title" style="left:330px;top:2434px">Help Link</h3>
  <ul class="abs links" style="left:332px;top:2478px"><li>Terms&amp;conditions</li><li>Privacy Policy</li><li>About Us</li><li>Support</li></ul>
  <h3 class="abs news-title">Subscribe To Our Newsletter</h3>
  <div class="abs field"><span>Enter Your Email</span><svg width="14" height="14" viewBox="0 0 14 14"><path d="M1 7l12-6-5 12-2-5z" fill="#f68a0f"/></svg></div>
  <div class="abs contact" style="left:592px">+ 188-555-0147</div>
  <div class="abs contact" style="left:738px;font-size:16px">info@quillstar.com</div>
  <div class="abs socials"><span></span><span></span><span></span><span></span></div>
  <div class="abs rule"></div>
  <p class="abs copy">©Copyrights 2022 &nbsp;Quillstar &nbsp;&nbsp;| &nbsp;&nbsp;All Rights Reserved</p>
</div>
</body>
</html>
```